Sunridge Pilates Centre
Business Cards
Bright & Fun-filled
Maribel Foster
Owner/Certified Pilates Instructor
2847 Kestrel Dr La Mesa CA 91873
n/A
do not have until sept 20
maribel@sunridgepilatescentre.com
www.sunridgepilatescentre.com
not sure but maybe? maybe logo or a Konrad Weller Quote or??

```html
<!DOCTYPE html>
<html lang="en">
<head>
<meta charset="utf-8">
<title>Sunridge Pilates Centre – Stationery</title>
<link href="https://fonts.googleapis.com/css2?family=Montserrat:wght@400;600&display=swap" rel="stylesheet">
<style>
  :root {
    --gold: #c9a04a;
    --gold-light: #e6c77e;
    --gold-dark: #a77f2e;
    --paper: #ffffff;
    --ink: #4a4a4a;
    --ink-soft: #8a8a8a;
    --backdrop: #f1f1f1;
  }
  * { margin: 0; padding: 0; box-sizing: border-box; }
  html, body { width: 1200px; height: 936px; overflow: hidden; }
  body {
    background: var(--backdrop);
    font-family: "Montserrat", Arial, sans-serif;
    color: var(--ink);
    position: relative;
  }
  .sheet {
    position: absolute;
    background: var(--paper);
    box-shadow: 0 2px 8px rgba(0,0,0,.18);
    overflow: hidden;
  }
  .sheet > svg.swoosh {
    position: absolute; inset: 0; width: 100%; height: 100%;
  }
  .brand {
    position: absolute;
    text-align: center;
    color: var(--gold);
    font-weight: 600;
    line-height: 1.1;
  }
  .brand .dot {
    display: block; margin: 0 auto 6%;
    border-radius: 50%; background: var(--gold);
  }

  /* Letterhead */
  .letterhead { left: 178px; top: 68px; width: 393px; height: 546px; }
  .letterhead .brand { left: 62px; top: 50px; width: 110px; font-size: 11px; }
  .letterhead .brand .dot { width: 26px; height: 26px; }
  .contact {
    position: absolute; left: 232px; top: 36px;
    font-size: 6px; line-height: 10px; color: var(--ink);
    list-style: none;
  }
  .contact li { display: flex; align-items: center; gap: 5px; }
  .contact svg { width: 7px; height: 7px; fill: var(--gold); }
  .letter {
    position: absolute; left: 36px; top: 162px; width: 300px;
    font-size: 5.4px; line-height: 8px; color: var(--ink-soft);
  }
  .letter p { margin-bottom: 9px; }
  .letter .signature-space { height: 26px; }
  .letter .signer { color: var(--ink); font-weight: 600; margin-bottom: 0; }

  /* Presentation page */
  .page { left: 634px; top: 38px; width: 462px; height: 576px; }
  .page .brand { left: 121px; top: 200px; width: 220px; font-size: 24px; }
  .page .brand .dot { width: 58px; height: 58px; }

  /* Business cards */
  .card { width: 175px; height: 106px; }
  .card-front { left: 46px; top: 655px; }
  .card-back { left: 46px; top: 784px; }
  .card-front .brand { left: 6px; top: 16px; width: 60px; font-size: 6.5px; }
  .card-front .brand .dot { width: 14px; height: 14px; }
  .card-front .holder {
    position: absolute; left: 70px; top: 18px; width: 88px;
    font-size: 4px; line-height: 6.5px;
  }
  .card-front .holder strong { color: var(--gold); font-weight: 600; font-size: 5.5px; }
  .card-front .holder .details { margin-top: 12px; color: var(--ink-soft); }
  .card-back .brand { left: 45px; top: 24px; width: 80px; font-size: 8px; }
  .card-back .brand .dot { width: 16px; height: 16px; }

  /* Envelopes */
  .envelope-front { left: 236px; top: 667px; width: 462px; height: 221px; }
  .envelope-front .brand { left: 30px; top: 22px; width: 110px; font-size: 11px; }
  .envelope-front .brand .dot { width: 24px; height: 24px; }
  .envelope-front .return {
    position: absolute; left: 28px; top: 100px; font-size: 5.5px; color: var(--ink-soft);
  }
  .envelope-back { left: 741px; top: 672px; width: 413px; height: 216px; }
  .envelope-back .web {
    position: absolute; left: 0; right: 0; top: 64px; text-align: center;
    font-size: 7px; letter-spacing: 2px; color: var(--paper);
  }
</style>
</head>
<body>

<svg width="0" height="0" aria-hidden="true" style="position:absolute">
  <defs>
    <linearGradient id="goldFill" x1="0" y1="0" x2="1" y2="1">
      <stop offset="0" stop-color="#e6c77e"/>
      <stop offset=".5" stop-color="#c9a04a"/>
      <stop offset="1" stop-color="#a77f2e"/>
    </linearGradient>
  </defs>
</svg>

<!-- Letterhead -->
<section class="sheet letterhead">
  <svg class="swoosh" viewBox="0 0 100 100" preserveAspectRatio="none" aria-hidden="true">
    <path d="M88 0 Q97 20 100 38 L100 0 Z" fill="url(#goldFill)"/>
    <path d="M85 0 Q95 18 97 40" fill="none" stroke="#c9a04a" stroke-width=".4"/>
    <path d="M100 72 Q96 90 86 100 L100 100 Z" fill="url(#goldFill)"/>
    <path d="M0 74 Q4 90 12 100" fill="none" stroke="#c9a04a" stroke-width=".5"/>
    <path d="M0 80 Q3 92 8 100 L0 100 Z" fill="url(#goldFill)"/>
  </svg>
  <div class="brand"><span class="dot"></span>Sunridge<br>Pilates Centre</div>
  <ul class="contact">
    <li><svg viewBox="0 0 10 10"><path d="M5 0a3.5 3.5 0 0 0-3.5 3.5C1.5 6 5 10 5 10s3.5-4 3.5-6.5A3.5 3.5 0 0 0 5 0zm0 5a1.5 1.5 0 1 1 0-3 1.5 1.5 0 0 1 0 3z"/></svg>2847 Kestrel Dr</li>
    <li><svg viewBox="0 0 10 10"><circle cx="5" cy="5" r="2"/></svg>La Mesa, CA 91873</li>
    <li><svg viewBox="0 0 10 10"><path d="M0 2h10v6H0z M0 2l5 3.5L10 2" /></svg>maribel@sunridgepilatescentre.com</li>
    <li><svg viewBox="0 0 10 10"><circle cx="5" cy="5" r="4.5"/></svg>www.sunridgepilatescentre.com</li>
  </ul>
  <div class="letter">
    <p>July 9, 2019</p>
    <p>Dear Client,<br>12 Harbor Lane, Suite 4</p>
    <p>Thank you for choosing our studio for your movement practice. Our classes blend strength, balance and breath so each session leaves you feeling lighter and more focused. We welcome every level, from first timers to seasoned teachers, in small supportive groups.</p>
    <p>Our reformer and mat sessions run through the week, with early and evening times to fit busy schedules. Private lessons are also available for anyone who wants focused attention on posture and recovery.</p>
    <p>Please reach out with any questions about memberships or class packs. We look forward to welcoming you to the studio soon.</p>
    <p>Kind Regards,</p>
    <div class="signature-space"></div>
    <p class="signer">Maribel Foster</p>
    <p>Studio Director</p>
  </div>
</section>

<!-- Presentation page -->
<section class="sheet page">
  <svg class="swoosh" viewBox="0 0 100 100" preserveAspectRatio="none" aria-hidden="true">
    <path d="M86 0 Q97 18 100 34 L100 0 Z" fill="url(#goldFill)"/>
    <path d="M83 0 Q95 16 97 36" fill="none" stroke="#c9a04a" stroke-width=".4"/>
    <path d="M100 70 Q96 90 84 100 L100 100 Z" fill="url(#goldFill)"/>
    <path d="M80 100 Q93 88 97 66" fill="none" stroke="#c9a04a" stroke-width=".4"/>
  </svg>
  <div class="brand"><span class="dot"></span>Sunridge<br>Pilates Centre</div>
</section>

<!-- Business card front -->
<section class="sheet card card-front">
  <svg class="swoosh" viewBox="0 0 100 100" preserveAspectRatio="none" aria-hidden="true">
    <path d="M92 0 Q100 40 96 100 L100 100 L100 0 Z" fill="url(#goldFill)"/>
  </svg>
  <div class="brand"><span class="dot"></span>Sunridge<br>Pilates Centre</div>
  <div class="holder">
    <strong>Maribel Foster</strong><br>Owner/Certified Pilates Instructor
    <div class="details">2847 Kestrel Dr<br>La Mesa CA 91873<br>maribel@sunridgepilatescentre.com<br>www.sunridgepilatescentre.com</div>
  </div>
</section>

<!-- Business card back -->
<section class="sheet card card-back">
  <svg class="swoosh" viewBox="0 0 100 100" preserveAspectRatio="none" aria-hidden="true">
    <path d="M0 0 Q8 50 3 100 L0 100 Z" fill="url(#goldFill)"/>
    <path d="M100 0 Q92 50 97 100 L100 100 Z" fill="url(#goldFill)"/>
  </svg>
  <div class="brand"><span class="dot"></span>Sunridge<br>Pilates Centre</div>
</section>

<!-- Envelope front -->
<section class="sheet envelope-front">
  <svg class="swoosh" viewBox="0 0 100 100" preserveAspectRatio="none" aria-hidden="true">
    <path d="M93 0 Q99 50 96 100 L100 100 L100 0 Z" fill="url(#goldFill)"/>
    <path d="M90 0 Q97 50 93 100" fill="none" stroke="#c9a04a" stroke-width=".3"/>
  </svg>
  <div class="brand"><span class="dot"></span>Sunridge<br>Pilates Centre</div>
  <p class="return">2847 Kestrel Dr, La Mesa, CA 91873</p>
</section>

<!-- Envelope back -->
<section class="sheet envelope-back">
  <svg class="swoosh" viewBox="0 0 100 100" preserveAspectRatio="none" aria-hidden="true">
    <path d="M0 0 H100 V44 Q50 32 0 44 Z" fill="url(#goldFill)"/>
  </svg>
  <p class="web">www.sunridgepilatescentre.com</p>
</section>

</body>
</html>
```